Vexel Business Cards

We need a new look business cvard to refelect our new look website www.vexel-example.com.au
We’re Vexel, a team of town planning and traffic and transport engineering specialists located in Melbourne.

Vexel is a company that is structured, articulate, dynamic, progressive, accurate and adaptable.
Our key messages are:
1. We make your life easier by doing what we do best
2. We tell you what you need to know not what you want to hear
3. Polished and professional but not afraid to show some personality

we would like a bold new look that is polished and professional but not afraid to show a bit of personality

Target Market(s)

Vexel’s diverse client base consists of architecture practices, builders, developers, local government and the legal fraternity.

Industry/Entity Type

Town

Requirements
Must have
• must use our logo and have the following information

Joel Harcastle
Director

Vexel Consultants Pty Ltd
Fernhollow first floor
Tamber Street
Larkfield VIC 3188 Australia
+61 03 9555 0187
mail@vexel-example.com.au
www.vexel-example.com.au
Nice to have
• We would like to see the logo used or the colours of the logo used.

```html
<!DOCTYPE html>
<html lang="en">
<head>
<meta charset="utf-8">
<title>Vexel Business Cards</title>
<link rel="stylesheet" href="https://fonts.googleapis.com/css2?family=Open+Sans:wght@400;600;700&display=swap">
<style>
  :root {
    --stage: #d9dadb;
    --slate: #7b8690;
    --orange: #f6931e;
    --white: #ffffff;
    --ink: #1c1c1c;
    --wordmark: #7a858e;
  }
  * { margin: 0; padding: 0; box-sizing: border-box; }
  html, body { width: 1200px; height: 900px; overflow: hidden; }
  body {
    background: var(--stage);
    font-family: "Open Sans", Arial, sans-serif;
    position: relative;
  }
  .card {
    position: absolute;
    width: 520px;
    height: 318px;
    top: 291px;
    overflow: hidden;
    box-shadow: 0 6px 18px rgba(0,0,0,0.18);
  }
  .card-back { left: 50px; background: var(--slate); }
  .card-front { left: 630px; background: var(--white); }

  .back-pattern {
    position: absolute;
    left: 0; top: 0;
    width: 330px; height: 318px;
    background: linear-gradient(135deg, rgba(255,255,255,0.22), rgba(255,255,255,0.05));
  }
  .back-name {
    position: absolute;
    right: 34px; bottom: 60px;
    color: var(--white);
    font-size: 78px;
    font-weight: 400;
    letter-spacing: -1px;
    line-height: 1;
  }

  .front-shapes { position: absolute; inset: 0; }
  .brand {
    position: absolute;
    left: 150px; top: 70px;
    display: flex; align-items: center; gap: 12px;
  }
  .brand-mark { width: 16px; height: 16px; background: var(--orange); }
  .brand-name {
    color: var(--wordmark);
    font-size: 44px;
    font-weight: 400;
    line-height: 1;
  }
  .address {
    position: absolute;
    left: 38px; top: 198px;
    color: var(--white);
    font-size: 11.5px;
    font-weight: 600;
    font-style: normal;
    line-height: 1.55;
  }
  .holder {
    position: absolute;
    left: 352px; top: 166px;
    color: var(--ink);
  }
  .holder-name { font-size: 15px; font-weight: 700; text-transform: uppercase; }
  .holder-role { font-size: 11px; }
  .contacts {
    position: absolute;
    left: 340px; top: 234px;
    list-style: none;
    font-size: 11px;
    color: var(--ink);
    line-height: 1.7;
  }
  .contacts li { display: flex; align-items: center; gap: 9px; white-space: nowrap; }
  .contacts svg { width: 13px; height: 13px; flex: none; }
</style>
</head>
<body>
  <section class="card card-back">
    <div class="back-pattern" role="img" aria-label="Faint tiled brand pattern"></div>
    <div class="back-name">Vexel</div>
  </section>

  <section class="card card-front">
    <svg class="front-shapes" viewBox="0 0 520 318" aria-hidden="true">
      <polygon points="0,0 38,0 24,22 40,42 0,42" fill="var(--slate)"/>
      <polygon points="0,168 328,168 300,318 0,318" fill="var(--orange)"/>
      <polygon points="330,152 520,152 520,318 300,318 328,168 322,160" fill="var(--slate)"/>
    </svg>
    <div class="brand">
      <span class="brand-mark"></span>
      <span class="brand-name">Vexel</span>
    </div>
    <address class="address">
      Vexel Consultants Pty Ltd<br>
      Fernhollow first floor<br>
      Tamber Street<br>
      Larkfield VIC 3188 Australia
    </address>
    <div class="holder">
      <div class="holder-name">Joel Harcastle</div>
      <div class="holder-role">Director</div>
    </div>
    <ul class="contacts">
      <li>
        <svg viewBox="0 0 14 14"><rect x="3.5" y="0.5" width="7" height="13" rx="1.5" fill="none" stroke="#1c1c1c"/><rect x="5" y="2.5" width="4" height="7" fill="#1c1c1c"/></svg>
        +61 03 9555 0187
      </li>
      <li>
        <svg viewBox="0 0 14 14"><rect x="0.5" y="2.5" width="13" height="9" fill="#1c1c1c"/><polyline points="0.5,2.5 7,8 13.5,2.5" fill="none" stroke="#7b8690"/></svg>
        mail@vexel-example.com.au
      </li>
      <li>
        <svg viewBox="0 0 14 14"><circle cx="7" cy="7" r="6.3" fill="#1c1c1c"/><ellipse cx="7" cy="7" rx="2.6" ry="6.3" fill="none" stroke="#7b8690" stroke-width="0.8"/><line x1="0.7" y1="7" x2="13.3" y2="7" stroke="#7b8690" stroke-width="0.8"/></svg>
        www.vexel-example.com.au
      </li>
    </ul>
  </section>
</body>
</html>
```